i need a business card for a plumbing company in california

we are a drain cleaning , maintenance plumbing company who is starting new marketing campaign for a tatrench-less pipe installation department .

Target Market(s)

the professional who appreciates time and quality workmanship.

Industry/Entity Type

Plumbing

Colors
0655a3
ec1f27

Requirements
Must have
• the second logo needs to be included
Nice to have
• a focus on the services offered
Should not have
• any underlined words on the brief

```html
<!DOCTYPE html>
<html lang="en">
<head>
<meta charset="utf-8">
<title>Flowline Plumbing – Business Card</title>
<link href="https://fonts.googleapis.com/css2?family=Arimo:wght@400;700&family=Exo+2:wght@700&display=swap" rel="stylesheet">
<style>
  :root {
    --brand-red: #ec1f27;
    --brand-blue: #0655a3;
    --logo-grey: #74746c;
    --ink: #2a2a2a;
    --card-white: #ffffff;
    --card-shade: #e9e9e9;
    --backdrop: #2e2e2e;
  }
  * { margin: 0; padding: 0; box-sizing: border-box; }
  html, body {
    width: 1200px;
    height: 997px;
    overflow: hidden;
    background: var(--backdrop);
    font-family: "Arimo", Arial, sans-serif;
  }
  .stage { position: relative; width: 1200px; height: 997px; }

  .card {
    position: absolute;
    width: 520px;
    height: 297px;
    border-radius: 18px;
    overflow: hidden;
    background: linear-gradient(160deg, var(--card-white) 0%, var(--card-white) 45%, var(--card-shade) 100%);
    box-shadow: 0 14px 30px rgba(0,0,0,.5);
  }
  .card-front { left: 90px; top: 150px; }
  .card-back  { left: 590px; top: 500px; }

  .wordmark {
    display: flex;
    align-items: center;
    gap: 12px;
    font-family: "Exo 2", Arial, sans-serif;
    font-weight: 700;
    color: var(--logo-grey);
    line-height: 0.95;
  }
  .wordmark-dot {
    width: 26px; height: 26px;
    border-radius: 50%;
    background: var(--brand-red);
    flex: none;
  }

  /* front */
  .card-front .wordmark {
    position: absolute;
    left: 0; right: 0; top: 92px;
    justify-content: center;
    font-size: 46px;
  }
  .services-band {
    position: absolute;
    left: 0; right: 0; bottom: 0;
    height: 46px;
    background: var(--brand-red);
    border-top: 4px solid var(--brand-blue);
    display: flex;
    align-items: center;
    justify-content: center;
    color: var(--card-white);
    font-weight: 700;
    font-size: 13px;
    font-variant: small-caps;
    letter-spacing: 1px;
  }

  /* back */
  .side-band {
    position: absolute;
    left: 0; top: 0; bottom: 0;
    width: 74px;
    background: var(--brand-red);
    border-right: 4px solid var(--brand-blue);
  }
  .card-back .wordmark {
    position: absolute;
    left: 170px; top: 44px;
    font-size: 36px;
  }
  .person { position: absolute; left: 118px; top: 150px; }
  .person-name {
    color: var(--brand-red);
    font-weight: 700;
    font-size: 18px;
    letter-spacing: .5px;
    text-transform: uppercase;
  }
  .person-role { color: var(--ink); font-size: 13px; margin-top: 3px; }
  .website {
    position: absolute;
    right: 30px; top: 160px;
    color: var(--brand-red);
    font-weight: 700;
    font-size: 14px;
  }
  .contact-icons {
    position: absolute;
    left: 56px; top: 218px;
    width: 26px; height: 58px;
    border-radius: 13px;
    background: var(--brand-blue);
    display: flex;
    flex-direction: column;
    align-items: center;
    justify-content: space-around;
    padding: 6px 0;
  }
  .contact-list {
    position: absolute;
    left: 118px; top: 222px;
    list-style: none;
    color: var(--ink);
    font-size: 15px;
    line-height: 28px;
  }
</style>
</head>
<body>
<main class="stage">

  <section class="card card-front" aria-label="Card front">
    <div class="wordmark"><span class="wordmark-dot"></span><span>Flowline Plumbing</span></div>
    <div class="services-band">Sewer Drain Cleaning, Maintenance, Trenchless Pipe Installs</div>
  </section>

  <section class="card card-back" aria-label="Card back">
    <div class="side-band"></div>
    <div class="wordmark"><span class="wordmark-dot"></span><span>Flowline<br>Plumbing</span></div>
    <div class="person">
      <p class="person-name">Daniel Reyes</p>
      <p class="person-role">Director</p>
    </div>
    <p class="website">www.flowlineplumbing.com</p>
    <div class="contact-icons" aria-hidden="true">
      <svg width="14" height="14" viewBox="0 0 24 24"><path fill="#fff" d="M6.6 10.8a15 15 0 0 0 6.6 6.6l2.2-2.2a1 1 0 0 1 1-.25 11.4 11.4 0 0 0 3.6.57 1 1 0 0 1 1 1V20a1 1 0 0 1-1 1A17 17 0 0 1 3 4a1 1 0 0 1 1-1h3.5a1 1 0 0 1 1 1c0 1.25.2 2.45.57 3.6a1 1 0 0 1-.25 1z"/></svg>
      <svg width="14" height="12" viewBox="0 0 24 20"><rect x="1" y="2" width="22" height="16" rx="2" fill="#fff"/><path d="M2 4l10 7 10-7" stroke="#0655a3" stroke-width="2" fill="none"/></svg>
    </div>
    <ul class="contact-list">
      <li>1441 555 0142</li>
      <li>dreyes@flowlineplumbing.com</li>
    </ul>
  </section>

</main>
</body>
</html>
```